BRIGHT LEDGER NOW

I'm virtually ready to launch my site, but I have a number of edits and modifications that need to be implemented. More importantly, I'm always looking to improve my site, particularly now that I am making my proverbial "FIRST IMPRESSION." Thus, I'm willing to see if there is someone who can add creativity and perhaps improve what I already have, particularly on the All Important Front Page.

Need extra days to review

```html
<!DOCTYPE html>
<html lang="en">
<head>
<meta charset="utf-8">
<title>Bright Ledger Now</title>
<link href="https://fonts.googleapis.com/css2?family=EB+Garamond:wght@400;500;600;700&family=Montserrat:wght@500;600;700;800&display=swap" rel="stylesheet">
<style>
:root{
  --navy:#0c1f4e;
  --navy-deep:#081838;
  --red:#b2121c;
  --mist:#eff1f5;
  --ink:#2d3344;
  --muted:#4a5060;
  --white:#ffffff;
  --rule:#c9cdd8;
}
*{margin:0;padding:0;box-sizing:border-box}
html,body{width:1200px;height:3782px;overflow:hidden}
body{position:relative;font-family:"EB Garamond",Georgia,serif;color:var(--ink);background:var(--white)}
.abs{position:absolute}
.sans{font-family:"Montserrat",Arial,sans-serif}

/* buttons */
.btn{position:absolute;display:flex;align-items:center;justify-content:center;gap:10px;font-family:"Montserrat",Arial,sans-serif;font-weight:700;font-size:10px;letter-spacing:.3px;color:var(--white);text-transform:uppercase;text-decoration:none}
.btn-red{background:var(--red)}
.btn-navy{background:var(--navy)}
.btn svg{width:10px;height:10px}

/* eyebrow labels */
.eyebrow{position:absolute;display:flex;align-items:center;gap:16px;font-family:"Montserrat",Arial,sans-serif;font-weight:700;font-size:11px;letter-spacing:2.6px;color:var(--red);text-transform:uppercase}
.eyebrow::before{content:"";width:66px;height:2px;background:var(--red)}

/* hero */
.hero{position:absolute;left:0;top:0;width:1200px;height:676px;overflow:hidden}
.hero-photo{position:absolute;inset:0;background:linear-gradient(90deg,#1a1d26 0%,#3b2e27 30%,#5a4536 55%,#2e2a2b 80%,#1b2232 100%)}
.hero-shade{position:absolute;left:0;right:0;top:0;bottom:0;background:linear-gradient(180deg,rgba(10,16,30,.35) 0%,rgba(10,16,30,.1) 25%,rgba(10,16,30,.35) 45%,rgba(10,16,30,.55) 75%,rgba(10,16,30,.3) 100%)}
.brand-badge{position:absolute;top:32px;width:116px;height:116px;border-radius:50%;background:var(--white);display:flex;align-items:center;justify-content:center;text-align:center;font-family:"EB Garamond",Georgia,serif;font-weight:700;font-size:14px;line-height:16px;color:var(--navy)}
.hero-title{position:absolute;top:32px;left:0;width:1200px;text-align:center;font-family:"Montserrat",Arial,sans-serif;font-weight:800;font-size:30px;color:var(--white);letter-spacing:.3px}
.hero-contact{position:absolute;top:72px;left:0;width:1200px;text-align:center;font-size:13px;line-height:19px;color:#e9e9ee}
.hero-kicker{position:absolute;top:297px;left:0;width:1200px;text-align:center;font-family:"Montserrat",Arial,sans-serif;font-weight:700;font-size:10.5px;letter-spacing:2.4px;color:var(--white)}
.hero-heading{position:absolute;top:318px;left:220px;width:760px;text-align:center;font-weight:600;font-size:29px;line-height:40px;color:var(--white)}
.hero-text{position:absolute;top:403px;left:270px;width:660px;text-align:center;font-size:15.5px;line-height:21.6px;color:#f0f0f3}
.hero-text strong{font-weight:700;color:var(--white)}

/* about */
.about-bg{position:absolute;left:729px;top:774px;width:471px;height:410px;background:var(--mist)}
.about-bar{position:absolute;left:610px;top:845px;width:30px;height:279px;background:var(--navy)}
.about-photo{position:absolute;left:640px;top:818px;width:459px;height:341px;background:linear-gradient(135deg,#8a8a73 0%,#b9b7a0 35%,#6e7a5c 60%,#c39a4c 85%,#8a8a73 100%)}
.section-heading{position:absolute;font-weight:700;font-size:39px;line-height:44px;color:var(--navy)}
.body-copy{position:absolute;font-size:15.3px;line-height:21.6px;color:var(--muted)}
.body-copy p+p{margin-top:21.6px}
.quote{position:absolute;left:610px;top:1188px;width:450px;font-size:15.5px;line-height:21.6px}
.quote strong{color:var(--navy);font-weight:600}
.quote span{color:var(--red)}

/* contact band */
.contact-band{position:absolute;left:0;top:1490px;width:1200px;height:177px;background:var(--navy);overflow:hidden}
.band-mark{position:absolute;left:-45px;top:-8px;width:193px;height:193px;border-radius:50%;background:rgba(255,255,255,.07)}
.band-heading{position:absolute;left:219px;top:72px;font-weight:600;font-size:40px;color:var(--white)}

/* services */
.services{position:absolute;left:0;top:1667px;width:1200px;height:1183px;background:var(--mist)}
.services-heading{position:absolute;left:150px;top:1806px;width:900px;text-align:center;font-weight:600;font-size:25px;line-height:31px;color:var(--navy)}
.card{position:absolute;width:286px;height:395px;background:var(--white)}
.card-photo{height:153px}
.card-title{margin-top:25px;text-align:center;font-family:"Montserrat",Arial,sans-serif;font-weight:700;font-size:12px;color:var(--navy);text-transform:uppercase}
.card-text{margin:12px auto 0;width:250px;text-align:center;font-size:12.6px;line-height:19.2px;color:var(--muted)}
.card .btn{left:79px;bottom:26px;width:128px;height:35px}

/* faq */
.faq-list{position:absolute;left:457px;top:2950px;width:593px;border-top:1.5px solid var(--rule)}
.faq-item{border-bottom:1.5px solid var(--rule);padding:0 0 0 10px}
.faq-q{display:flex;align-items:center;gap:24px;min-height:61px;font-family:"Montserrat",Arial,sans-serif;font-weight:700;font-size:15px;line-height:19.5px;color:var(--navy)}
.faq-q .sign{width:14px;flex:0 0 14px;color:var(--red);font-size:22px;font-weight:600;text-align:center}
.faq-a{margin:-2px 0 0 38px;padding-bottom:24px;font-size:15.3px;line-height:21.6px;color:var(--muted)}

/* footer */
.footer{position:absolute;left:0;top:3479px;width:1200px;height:303px;background:var(--navy)}
.footer-badge{position:absolute;left:150px;top:73px;width:132px;height:132px;border-radius:50%;background:var(--white);display:flex;align-items:center;justify-content:center;text-align:center;font-weight:700;font-size:16px;line-height:19px;color:var(--navy)}
.footer-text{position:absolute;font-size:12.5px;line-height:19px;color:#dfe3ee}
.footer-links{position:absolute;list-style:none;font-size:12.5px;line-height:28.5px;color:#dfe3ee}
.social{position:absolute;left:1025px;width:22px;height:22px;border-radius:50%;background:var(--white)}
.footer-rule{position:absolute;left:150px;top:258px;width:900px;height:1px;background:rgba(255,255,255,.2)}
.copyright{position:absolute;left:0;top:272px;width:1200px;text-align:center;font-size:9.5px;color:#c7ccda}
</style>
</head>
<body>

<!-- hero -->
<header class="hero">
  <div class="hero-photo" role="img" aria-label="Photo of a courtroom with an attorney addressing the judge's bench"></div>
  <div class="hero-shade"></div>
  <div class="brand-badge" style="left:62px">BRIGHT<br>LEDGER<br>NOW</div>
  <div class="brand-badge" style="left:1023px">BRIGHT<br>LEDGER<br>NOW</div>
  <h1 class="hero-title">BRIGHT LEDGER NOW</h1>
  <div class="hero-contact">4820 East Canyon Rd., Suite 210<br>Mesa, Arizona 85201<br>480.555.0142 / 800.555.0187<br>WWW.BRIGHTLEDGERNOW.COM</div>
  <div class="hero-kicker">BUSINESS OWNERS</div>
  <h2 class="hero-heading">Bright Ledger Now (BLN) is an extremely affordable legal service plan (as little as $8.00 per month)</h2>
  <p class="hero-text">It INSULATES business owners from unwarranted LEGAL CLAIMS and expensive LAWSUITS. Our plan uses local, experienced, quality attorneys who focus on PROBLEM PREVENTION using proprietary tools available only to BLN members. Contact us for a free consultation and receive a FREE OVERVIEW of your business to see if you are truly insulated from legal claims.<br><strong>Contact us to find out how you can join us to BRIGHT LEDGER NOW!!</strong></p>
  <a class="btn btn-red" style="left:407px;top:533px;width:135px;height:34px">Learn more <svg viewBox="0 0 10 10"><path d="M2 8 8 2M3 2h5v5" fill="none" stroke="#fff" stroke-width="1.6"/></svg></a>
  <a class="btn btn-navy" style="left:560px;top:533px;width:232px;height:34px">Schedule free consultation <svg viewBox="0 0 10 10"><path d="M2 8 8 2M3 2h5v5" fill="none" stroke="#fff" stroke-width="1.6"/></svg></a>
</header>

<!-- about -->
<section class="about">
  <div class="about-bg"></div>
  <div class="about-bar"></div>
  <div class="about-photo" role="img" aria-label="Close-up photo of a banknote portrait wearing a face mask"></div>
  <div class="eyebrow" style="left:150px;top:802px">About us</div>
  <h2 class="section-heading" style="left:150px;top:848px">We can Protect You.</h2>
  <div class="body-copy" style="left:150px;top:920px;width:440px">
    <p>BLN is a group of attorney and legal assistants with many years of experience in litigation, who are devoted to PREVENTING LEGAL CLAIMS and COSTLY LAWSUITS through a variety of FREE and VERY AFFORDABLE services described below.<br>OUR UNIQUE SERVICE PLAN MAKES IT POSSIBLE FOR US TO BRIGHT LEDGER NOW.</p>
    <p>A homebuilding company was sued by a former employee who claimed to have been promised a more favorable sales area, which claim was disputed by the homebuilder. There was no evidence that such a promise had been made, other than the plaintiff's oral testimony. The company had the case dismissed, but spent $10,000 defending the case.</p>
    <p>And even though it was awarded its attorney's fees, the plaintiff proved uncollectible. Had the company been an BLN member, the case likely would never have been filed. Call for your FREE CONSULTATION and let us show you why the plaintiff likely would not have found a contingency attorney (as was the case) or been able to pay an attorney on an hourly basis. In short, by using BLN's services, the plaintiff's claim would not have been filed.</p>
  </div>
  <p class="quote"><strong>“An OUNCE of PREVENTION is worth a POUND of CURE.”</strong><br><span>&nbsp;-Harold Whitmore.</span></p>
  <div class="body-copy" style="left:610px;top:1263px;width:445px">
    <p>In our vast experience with commercial litigation, we believe that a very large percentage of litigation cases hinge on "he said / she said" issues. By using BLN's services, we believe we can INSULATE you and your business from all such issues, which will MINIMIZE your EXPOSURE to LEGAL CLAIMS and LAWSUITS.</p>
  </div>
</section>

<!-- contact band -->
<section class="contact-band">
  <div class="band-mark"></div>
  <div class="eyebrow" style="left:219px;top:48px">We can assist you</div>
  <h2 class="band-heading">Contact Us for a FREE Consultation</h2>
  <a class="btn btn-red" style="left:899px;top:73px;width:151px;height:35px">Schedule now <svg viewBox="0 0 10 10"><path d="M2 8 8 2M3 2h5v5" fill="none" stroke="#fff" stroke-width="1.6"/></svg></a>
</section>

<!-- services -->
<section class="services"></section>
<div class="eyebrow" style="left:500px;top:1773px">Our services</div>
<h2 class="services-heading">The price for a membership is a ridiculously low $9.95 PER WEEK. We believe that this fee is very affordable. So what is it? Membership includes the following:</h2>

<article class="card" style="left:150px;top:1905px">
  <div class="card-photo" role="img" aria-label="Photo of an attorney consulting with a client beside scales of justice" style="background:linear-gradient(120deg,#3a2a22,#8a6b4c 50%,#c9b79a)"></div>
  <h3 class="card-title">Free Initial Consultation</h3>
  <p class="card-text">As a prospective Bright Ledger Now (“BLN”) member, we urge you to schedule an initial consultation with us – at no charge – where we will go over each of the services in detail, and offer an overview of your business formation at no charge.</p>
  <a class="btn btn-red">Lean more <svg viewBox="0 0 10 10"><path d="M2 8 8 2M3 2h5v5" fill="none" stroke="#fff" stroke-width="1.6"/></svg></a>
</article>
<article class="card" style="left:457px;top:1905px">
  <div class="card-photo" role="img" aria-label="Photo of a hand signing a contract document" style="background:linear-gradient(120deg,#d8d8d6,#a9a7a3 50%,#3d3a38)"></div>
  <h3 class="card-title">Proprietary Contract Language</h3>
  <p class="card-text">BLN members are entitled to incorporate exclusive proprietary contract language in their contracts, work orders, and other written agreements in their business, that MINIMIZES EXPOSURE to legal claims against your business.</p>
  <a class="btn btn-red">Learn more <svg viewBox="0 0 10 10"><path d="M2 8 8 2M3 2h5v5" fill="none" stroke="#fff" stroke-width="1.6"/></svg></a>
</article>
<article class="card" style="left:764px;top:1905px">
  <div class="card-photo" role="img" aria-label="Photo of business people reviewing papers at a desk" style="background:linear-gradient(120deg,#2a2c30,#6b6e73 50%,#b9b4a8)"></div>
  <h3 class="card-title">Free Consultation</h3>
  <p class="card-text">BLN members can call their local BLN Attorney any time, and be given a 30 minute consultation, free of charge, once per month. The value of this cannot be overstated and easily pays for the membership - many times over.</p>
  <a class="btn btn-red">Learn more <svg viewBox="0 0 10 10"><path d="M2 8 8 2M3 2h5v5" fill="none" stroke="#fff" stroke-width="1.6"/></svg></a>
</article>
<article class="card" style="left:150px;top:2323px">
  <div class="card-photo" role="img" aria-label="Photo of a letter being handed across a wooden table" style="background:linear-gradient(120deg,#5c6b7a,#b08a5e 50%,#8a5a32)"></div>
  <h3 class="card-title">Free Attorney Letters</h3>
  <p class="card-text">In addition to free monthly consultations, BLN members can have their local BLN Attorney send out a letter regarding their business, once per month, at no charge.</p>
  <a class="btn btn-red">Learn more <svg viewBox="0 0 10 10"><path d="M2 8 8 2M3 2h5v5" fill="none" stroke="#fff" stroke-width="1.6"/></svg></a>
</article>
<article class="card" style="left:457px;top:2323px">
  <div class="card-photo" role="img" aria-label="Photo of a gavel resting on a pile of banknotes" style="background:linear-gradient(120deg,#9aa39a,#6d5140 50%,#b7bdb3)"></div>
  <h3 class="card-title">Litigation Discounts</h3>
  <p class="card-text">BLN members who use the Proprietary Contract Language described above are given considerable discounts, including flat fee discounts, in the even of defensive litigation.</p>
  <a class="btn btn-red">Learn more <svg viewBox="0 0 10 10"><path d="M2 8 8 2M3 2h5v5" fill="none" stroke="#fff" stroke-width="1.6"/></svg></a>
</article>
<article class="card" style="left:764px;top:2323px">
  <div class="card-photo" role="img" aria-label="Photo of a gavel, books and glasses on a dark desk" style="background:linear-gradient(120deg,#2b2620,#5a4a36 55%,#1e1b17)"></div>
  <h3 class="card-title">Collections</h3>
  <p class="card-text">BLN members can have their BLN Attorney pursue collection claims on a contingency fee basis, provided the claim is based on a contract.</p>
  <a class="btn btn-red">Learn more <svg viewBox="0 0 10 10"><path d="M2 8 8 2M3 2h5v5" fill="none" stroke="#fff" stroke-width="1.6"/></svg></a>
</article>

<!-- faq -->
<section class="faq">
  <div class="eyebrow" style="left:150px;top:2944px">FAQs</div>
  <h2 class="section-heading" style="left:150px;top:2982px">Have any<br>Questions?</h2>
  <div class="faq-list">
    <div class="faq-item"><div class="faq-q"><span class="sign">+</span>Why should I be concerned about legal claims?</div></div>
    <div class="faq-item"><div class="faq-q"><span class="sign">−</span>Provide more details about the value of BLN's contract language.</div>
      <p class="faq-a">Lorem ipsum dolor sit amet, consectetur adipiscing elit. Suspendisse varius enim in eros elementum tristique. Duis cursus, mi quis viverra ornare, eros dolor interdum nulla, ut commodo diam libero vitae erat.</p></div>
    <div class="faq-item"><div class="faq-q" style="min-height:82px"><span class="sign">+</span>If I'm a contractor, for example, how can an BLN membership minimize legal claims against my business?</div></div>
    <div class="faq-item"><div class="faq-q" style="min-height:63px"><span class="sign">+</span>What does an BLN membership cost?</div></div>
    <div class="faq-item"><div class="faq-q" style="min-height:63px"><span class="sign">+</span>Do you have a Referral Program?</div></div>
  </div>
</section>

<!-- footer -->
<footer class="footer">
  <div class="footer-badge">BRIGHT<br>LEDGER<br>NOW</div>
  <p class="footer-text" style="left:392px;top:78px">(480) 555-0142 / (800) 555-0187</p>
  <p class="footer-text" style="left:392px;top:112px">4820 East Canyon Rd., Suite 210,<br>Mesa, Arizona 85201</p>
  <ul class="footer-links" style="left:683px;top:71px"><li>Home</li><li>About</li><li>Services</li><li>FAQ</li></ul>
  <ul class="footer-links" style="left:831px;top:71px"><li>Contact Us</li><li>Terms of Service</li><li>Privacy Policy</li></ul>
  <span class="social" style="top:81px" aria-label="Social link"></span>
  <span class="social" style="top:116px" aria-label="Social link"></span>
  <span class="social" style="top:153px" aria-label="Social link"></span>
  <div class="footer-rule"></div>
  <p class="copyright">© Copyright 2024 Brightledgernow. All Rights Reserved.</p>
</footer>

</body>
</html>
```